Bref créative
Modern Business Name Card for IT Company
qLumio Sdn Bhd
Simple
Marissa Tanaka
Senior Manager
Lot C-17, 5B Floor,
8 Kilner Plaza,
No. 7, Jalan 24/6
47810 Petaling Jaya
Selangor, Malaysia
marissa@qlumiomarketing.example
www.qlumiomarketing.example
2187605-K
Kindly change the tagline of the website to a different font Segoe UI Semibold since the current font seem to rough and thick. Thanks.

```html
<!DOCTYPE html>
<html lang="en">
<head>
<meta charset="utf-8">
<title>qLumio Sdn Bhd – Business Card</title>
<link href="https://fonts.googleapis.com/css2?family=Open+Sans:wght@600&display=swap" rel="stylesheet">
<style>
  :root {
    --page-bg: #e9ebef;
    --card-white: #ffffff;
    --brand-blue: #1d3c8f;
    --band-blue-deep: #0d2a78;
    --band-blue-mid: #1f4fb4;
    --band-blue-light: #2f66c8;
    --swoosh-green: #7cc242;
    --swoosh-green-light: #c4e59a;
    --text-on-blue: #ffffff;
    --title-on-blue: #d6e4ff;
  }
  * { box-sizing: border-box; margin: 0; padding: 0; }
  html, body {
    width: 1200px; height: 900px; overflow: hidden;
    background: var(--page-bg);
  }
  .business-card {
    position: absolute; left: 75px; top: 150px;
    width: 1050px; height: 600px;
    background: var(--card-white);
    overflow: hidden;
    box-shadow: 0 10px 30px rgba(0,0,0,.18);
    font-family: "Segoe UI Semibold", "Segoe UI", "Open Sans", sans-serif;
    font-weight: 600;
  }
  .card-waves { position: absolute; inset: 0; width: 100%; height: 100%; }
  .brand {
    position: absolute; left: 410px; top: 110px;
    display: flex; align-items: center; gap: 18px;
  }
  .brand-dot {
    width: 62px; height: 62px; border-radius: 50%;
    background: var(--swoosh-green);
  }
  .brand-name {
    font-size: 78px; line-height: 1; color: var(--brand-blue); letter-spacing: 1px;
  }
  .contact-list {
    position: absolute; left: 40px; top: 392px;
    list-style: none; color: var(--text-on-blue);
    font-size: 16px; line-height: 24px; letter-spacing: .3px;
  }
  .contact-list li { display: flex; gap: 8px; align-items: flex-start; }
  .contact-icon {
    flex: none; width: 18px; height: 18px; margin-top: 3px;
    border-radius: 50%; background: var(--text-on-blue);
    display: flex; align-items: center; justify-content: center;
  }
  .contact-icon svg { width: 12px; height: 12px; }
  .icon-fill { fill: var(--band-blue-mid); }
  .icon-line { fill: none; stroke: var(--band-blue-mid); stroke-width: .9; }
  .person {
    position: absolute; right: 70px; top: 396px; text-align: right;
  }
  .person-name {
    font-size: 24px; color: var(--text-on-blue); letter-spacing: 1.5px;
    text-transform: uppercase;
  }
  .person-title {
    margin-top: 6px; font-size: 17px; color: var(--title-on-blue);
    letter-spacing: 1px;
  }
</style>
</head>
<body>
<article class="business-card">
  <svg class="card-waves" viewBox="0 0 1050 600" preserveAspectRatio="none" aria-hidden="true">
    <defs>
      <linearGradient id="bandBlue" x1="0" y1="0" x2="1" y2="1">
        <stop offset="0" stop-color="#1f4fb4"/>
        <stop offset=".5" stop-color="#2f66c8"/>
        <stop offset="1" stop-color="#0d2a78"/>
      </linearGradient>
    </defs>
    <path d="M0,340 C220,270 470,300 690,290 C870,282 980,250 1050,235 L1050,275 C960,300 850,318 690,322 C470,330 230,300 0,372 Z" fill="#c4e59a"/>
    <path d="M0,352 C230,290 480,318 700,306 C880,296 985,262 1050,250 L1050,290 C970,312 860,330 700,336 C470,344 240,318 0,378 Z" fill="#7cc242"/>
    <path d="M0,372 C240,312 480,338 700,330 C880,322 985,290 1050,278 L1050,600 L0,600 Z" fill="url(#bandBlue)"/>
  </svg>

  <div class="brand">
    <span class="brand-dot"></span>
    <span class="brand-name">qLumio</span>
  </div>

  <ul class="contact-list">
    <li>
      <span class="contact-icon"><svg viewBox="0 0 12 12"><path class="icon-fill" d="M6 1a3.5 3.5 0 0 0-3.5 3.5C2.5 7.5 6 11 6 11s3.5-3.5 3.5-6.5A3.5 3.5 0 0 0 6 1zm0 4.8a1.3 1.3 0 1 1 0-2.6 1.3 1.3 0 0 1 0 2.6z"/></svg></span>
      <span>Lot C-17, 5B Floor, 8 Kilner Plaza,<br>No. 7, Jalan 24/6 47810 Petaling<br>Jaya Selangor, Malaysia</span>
    </li>
    <li>
      <span class="contact-icon"><svg viewBox="0 0 12 12"><path class="icon-fill" d="M3 1.5l1.6 2.2-.9 1.1a6 6 0 0 0 3.5 3.5l1.1-.9 2.2 1.6-.8 1.5C5.5 10.3 1.7 6.5 1.5 2.3z"/></svg></span>
      <span>60375550142</span>
    </li>
    <li>
      <span class="contact-icon"><svg viewBox="0 0 12 12"><rect class="icon-line" x="1.8" y="3.2" width="8.4" height="5.6"/><path class="icon-line" d="M1.8 3.3L6 6.5l4.2-3.2"/></svg></span>
      <span>marissa@qlumiomarketing.example</span>
    </li>
    <li>
      <span class="contact-icon"><svg viewBox="0 0 12 12"><circle class="icon-line" cx="6" cy="6" r="4.5"/><path class="icon-line" d="M1.5 6h9M6 1.5c-2 2.5-2 6.5 0 9M6 1.5c2 2.5 2 6.5 0 9"/></svg></span>
      <span>www.qlumiomarketing.example</span>
    </li>
    <li><span>License # : 2187605-K</span></li>
  </ul>

  <div class="person">
    <p class="person-name">Marissa Tanaka</p>
    <p class="person-title">Senior Manager</p>
  </div>
</article>
</body>
</html>
```